Health product web design

I have two websites that look terrible.  They are both 'bee' products related.  The text and links to pages are correct, I just need change the designs.
We are a health product company that sells a range of health and therapeutic products that come from the beehive; including bee pollen, Royal Jelly and Propolis.
The sites to be designed are not ecommerce sites.  They are more information sites that re-direct to our online store (soon to be redesigned) www.corvantaline.com.au
The sites I need revamped are:
www.mellowbrix.com.au
www.tarnivex.com.au
Royal Jelly is a substance made by the worker bees and fed to the Queen Bee.  People take Royal Jelly as it is high in a range of B group vitamins and helps increase energy levels, including sexual stamina.
Propolis is antibacterial, antiviral and has an anesthetic quality.  It is used to put on cuts, burns, sore throats, pimples and mouth & stomach ulcers.  Propolis is collected by bees from the sap of trees and used in the bee hive to sterilise it.
You can read the text (there isnt much) on each site to get an idea of what the products are good for.
The design should be colourful but also communicate credability, trust and a healthy lifestyle with an element of science as the products are sold as health and therapeutic related ie. capsules, liquids, ointments etc.
I am open to questions if you need further information.
Thanks

Target Market(s)
Target market is health supplement buyers 40 - 70 yrs
Industry/Entity Type
Health Product
Requirements
Must have
- Both sites will need a basic logo
Lifestyle images - images of healthy 35ish year old people and/or couples
Nice to have
- Images of bee hives
Close up images of bees, flowers
Images of nature

```html
<!DOCTYPE html>
<html lang="en">
<head>
<meta charset="utf-8">
<title>Tarnivex Australian Honey</title>
<link rel="stylesheet" href="https://fonts.googleapis.com/css2?family=Arimo:wght@400;700&display=swap">
<style>
:root{
  --bg-top:#8a3207;
  --bg-mid:#b8621f;
  --bg-low:#f3cf8e;
  --bg-foot:#fbecc6;
  --panel:#fffdf7;
  --panel-edge:#f3d6a1;
  --rule:#c4532a;
  --nav-box:#4d1304;
  --btn-top:#b2521c;
  --btn-bot:#7c2708;
  --btn-home-top:#ffd84a;
  --btn-home-bot:#e89c06;
  --heading:#b5330f;
  --text:#333333;
  --light:#ffffff;
  --honey-a:#fbe17a;
  --honey-b:#e0a214;
  --grass-a:#9fd16a;
  --grass-b:#3c8a1c;
}
*{box-sizing:border-box;margin:0;padding:0}
html,body{width:1069px;height:1200px;overflow:hidden}
body{
  font-family:"Arimo",Arial,sans-serif;
  background:linear-gradient(180deg,var(--bg-top) 0,var(--bg-mid) 330px,#d9934a 700px,var(--bg-low) 1000px,var(--bg-foot) 1070px,var(--bg-foot) 1200px);
  position:relative;
}
.header-tab{
  position:absolute;left:185px;top:13px;width:164px;height:80px;
  border-radius:82px 82px 0 0;background:var(--panel);
}
.header{
  position:absolute;left:34px;top:68px;width:1010px;height:248px;border-radius:14px;
  background:radial-gradient(ellipse at 50% 45%,var(--panel) 70%,var(--panel-edge) 100%);
}
.wordmark{
  position:absolute;left:60px;top:172px;width:440px;text-align:center;
  font-family:"Arimo",Arial,sans-serif;font-weight:400;font-size:32px;line-height:40px;
  color:var(--heading);
}
.header-photo{
  position:absolute;left:600px;top:85px;width:371px;height:226px;border-radius:40% 40% 45% 45%;
  background:radial-gradient(ellipse at 45% 55%,var(--honey-a),var(--honey-b) 70%,rgba(224,162,20,0) 100%);
}
.tagline{
  position:absolute;left:730px;top:246px;font-family:"Arimo",Arial,sans-serif;
  font-size:24px;font-weight:400;color:var(--heading);
}
.main{
  position:absolute;left:34px;top:338px;width:1010px;height:709px;border-radius:14px;
  border:1px solid var(--rule);
  background:radial-gradient(ellipse at 50% 50%,var(--panel) 85%,var(--panel-edge) 100%);
}
.nav{
  position:absolute;left:48px;top:352px;width:283px;height:322px;border-radius:9px;background:var(--nav-box);
  list-style:none;
}
.nav li{
  position:absolute;left:10px;width:263px;height:44px;border-radius:9px;
  background:linear-gradient(180deg,var(--btn-top),var(--btn-bot));
  color:var(--light);font-size:16px;line-height:44px;padding-left:19px;
}
.nav li.active{background:linear-gradient(180deg,var(--btn-home-top),var(--btn-home-bot));padding-left:15px}
.nav li.shop{padding-left:15px}
.feeds{
  position:absolute;left:48px;top:685px;width:283px;height:343px;border-radius:9px;background:var(--nav-box);
  color:var(--light);
}
.feeds h2{font-weight:400;font-size:16px;text-align:center;margin-top:18px;margin-right:20px}
.feeds p{font-size:12.5px;line-height:19.6px;margin:9px 34px 0 21px}
.feeds p+p{margin-top:19px}
.feeds .more{position:absolute;right:24px;bottom:10px;font-size:11px}
.content{position:absolute;left:368px;top:363px;width:650px;color:var(--text)}
.content h1{font-weight:400;font-size:19.5px;color:var(--heading);margin-left:-5px;margin-bottom:16px}
.content p{font-size:13px;line-height:22.9px;margin-bottom:22.9px}
.spoon-photo{
  float:right;width:330px;height:246px;margin:0 0 0 32px;
  background:radial-gradient(ellipse at 60% 40%,#fff6c2,#f7d23a 55%,#e8b20e);
  border:3px solid #fff;box-shadow:2px 3px 5px rgba(0,0,0,.35);
}
.jars-photo{
  position:absolute;left:366px;top:804px;width:329px;height:216px;border:1px solid #000;
  background:linear-gradient(180deg,#f4efe6,#d8a85a 55%,#a2431a);
}
.side-text{position:absolute;left:716px;top:807px;width:292px;color:var(--text);font-size:13px;line-height:22.9px}
.side-text p+p{margin-top:22.9px}
.footer{
  position:absolute;left:0;width:1069px;top:1083px;text-align:center;color:#333;font-size:12.5px;line-height:20px;
  padding-left:13px;
}
.grass{
  position:absolute;left:0;top:1145px;width:1069px;height:55px;
  background:linear-gradient(180deg,rgba(159,209,106,0),var(--grass-a) 35%,var(--grass-b));
}
.bee{
  position:absolute;left:0;top:1069px;width:191px;height:120px;border-radius:50%;
  background:radial-gradient(ellipse at 60% 55%,#f5e23a,#c9b015 55%,rgba(201,176,21,0) 72%);
}
</style>
</head>
<body>
  <div class="header-tab"></div>
  <header class="header"></header>
  <div class="wordmark">Tarnivex Australian Honey</div>
  <div class="header-photo" role="img" aria-label="Jar of honey with honeycomb and a wooden dipper in a glass bowl"></div>
  <div class="tagline">Sweeten your day!</div>

  <div class="main"></div>

  <ul class="nav">
    <li class="active" style="top:13px">Home</li>
    <li style="top:62px">What is Propolis?</li>
    <li style="top:112px">The benefits of Propolis</li>
    <li style="top:161px">Is Propolis safe?</li>
    <li style="top:210px">How is Propolis collected?</li>
    <li class="shop" style="top:261px">Buy Verdanel™ Propolis online</li>
  </ul>

  <aside class="feeds">
    <h2>Information Feeds</h2>
    <p>Is propolis Safe?<br>For the majority of people Propolis, and other bee products such as Royal Jelly, arecompletely safe.</p>
    <p>However, Propolis has been reported to cause allergic reactions in rare cases and isnot suitable for use by women who are pregnant or breastfeeding.</p>
    <p>If irritation of the mouth or throat occurs after taking Propolis, please<br>&nbsp;discontinue use.</p>
    <span class="more">more &nbsp;&gt;&gt;</span>
  </aside>

  <main class="content">
    <h1>Welcome to Tarnivex Australian Honey</h1>
    <div class="spoon-photo" role="img" aria-label="Spoon lifting golden honey from a glass jar"></div>
    <p>Propolis is a natural antibiotic used by bees to protect their hive from infection – and used by humans to boost their immune systems and fight infection.</p>
    <p>With powerful antibacterial, antiviral, antiseptic and antifungal properties, Propolis can be applied directly to the skin to sterilise minor cuts and wounds, used as a mouth spray to assist in good oral health, or taken in capsule or liquid form to assist in general immunity boosting.</p>
    <p>Unlike conventional antibiotics, Propolis has also<br>been found to be effective in assisting the body to fight viruses . Propolis is nutritious, rich in amino acids and antioxidant bioflavonoids, high in vitamins, and contains 14 of the 15 minerals needed by our bodies for normal function .</p>
  </main>

  <div class="jars-photo" role="img" aria-label="Row of honey jars and a squeeze bottle of Australian honey"></div>
  <div class="side-text">
    <p>Propolis is a dark resinous material produced by bees to seal and sterilise their hives – and used by humans to strengthen and seal the "cracks" in their immune system.</p>
    <p>Each hive colony includes several specialist, Propolis-manufacturing bees, who forage for tree resin on warm days when the substance is soft and pliable.</p>
  </div>

  <div class="grass" role="img" aria-label="Strip of green grass along the bottom edge"></div>
  <div class="bee" role="img" aria-label="Cartoon bee flying in the lower left corner"></div>
  <footer class="footer">
    (C) Tarnivex Natural Australian Honey. 2011<br>
    Information within this site is not intended to be a substitute for professional medical advice.
  </footer>
</body>
</html>
```